Design a visually appealing layout for our company mission and values. I want to create a visually appealing 1 page flyer that presents our company mission and values to clients as well as to our internal team/staff. We will utilize the 1 page flyer in internal and external presentations about our company. We will also use the flyer in sales proposals/marketing packages.

Target Market(s)

Internal team members as well as external prospective clients, existing clients & referral partners

Industry/Entity Type

Financial Service

Colors

Designer to choose colors to be used in the design.

Requirements
Must have
• Should reflect our company brand so I have included our Pantone panel, fonts etc. I have provided our company logo as well which should be part of the branded document
Nice to have
• I would like the presentation to be useable in different formats and to different audiences so something that is more graphic/visual heavy - otherwise it's a lot of words that people don't read.
• Would like to be able to easily include in our corporate template powerpoint presentation.

```html
<!DOCTYPE html>
<html lang="en">
<head>
<meta charset="utf-8">
<title>Summit Pension Partners – Our Mission</title>
<link href="https://fonts.googleapis.com/css2?family=Montserrat:wght@400;500;600;700;800&display=swap" rel="stylesheet">
<style>
  :root{
    --navy:#17365f;
    --navy-deep:#112a4b;
    --blue:#1f6fb6;
    --green:#8cc63f;
    --green-dark:#5e8f2a;
    --green-soft:#c9e7a1;
    --white:#ffffff;
    --ink:#1d3557;
  }
  *{margin:0;padding:0;box-sizing:border-box}
  html,body{width:900px;height:1200px;overflow:hidden;background:var(--white)}
  body{font-family:"Montserrat",Arial,sans-serif;color:var(--ink)}
  .flyer{position:relative;width:900px;height:1200px;overflow:hidden}
  .top-rule{position:absolute;top:0;left:0;width:900px;height:10px;background:var(--blue)}
  .hero-photo{
    position:absolute;left:0;top:10px;width:370px;height:570px;
    background:linear-gradient(160deg,#e8e6e2 0%,#c9c3bb 40%,#8c99a8 75%,#5d7390 100%);
  }
  .brand{position:absolute;top:80px;right:50px;display:flex;align-items:center;gap:14px}
  .brand-square{width:46px;height:46px;background:var(--green)}
  .brand-name{font-size:24px;font-weight:700;color:var(--navy);line-height:1.1;letter-spacing:.5px}
  .mission{position:absolute;top:270px;left:380px;width:510px;text-align:center}
  .mission h1{font-size:56px;font-weight:800;color:var(--blue);letter-spacing:1px;line-height:1;white-space:nowrap}
  .mission p{margin-top:18px;font-size:25px;font-weight:700;color:var(--navy);line-height:1.25;text-transform:uppercase}
  .values{
    position:absolute;left:0;top:580px;width:900px;height:620px;
    background:linear-gradient(180deg,var(--navy) 0%,var(--navy-deep) 100%);
  }
  .row{position:absolute;left:0;width:900px;display:flex;justify-content:center;gap:22px}
  .row-one{top:40px}
  .row-two{top:320px}
  .value{width:198px;display:flex;flex-direction:column;align-items:center}
  .value-icon{width:84px;height:84px;border-radius:50%;background:var(--green);border:4px solid var(--green-dark);display:flex;align-items:center;justify-content:center}
  .value-icon svg{width:44px;height:44px;fill:none;stroke:var(--white);stroke-width:2.4;stroke-linecap:round;stroke-linejoin:round}
  .value-body{align-self:flex-start;margin-top:16px}
  .value h2{font-size:17px;font-weight:800;color:var(--white);text-transform:uppercase;line-height:1.2}
  .value p{margin-top:6px;font-size:13px;font-weight:500;color:var(--green-soft);line-height:1.4}
</style>
</head>
<body>
<div class="flyer">
  <div class="top-rule"></div>
  <div class="hero-photo" role="img" aria-label="Photo of a smiling professional woman raising a fist in celebration"></div>

  <div class="brand">
    <div class="brand-square"></div>
    <div class="brand-name">SUMMIT PENSION<br>PARTNERS</div>
  </div>

  <section class="mission">
    <h1>OUR MISSION</h1>
    <p>To proactively support<br>organizations and<br>lead them toward<br>a secure future</p>
  </section>

  <section class="values">
    <div class="row row-one">
      <article class="value">
        <div class="value-icon"><svg viewBox="0 0 48 48"><circle cx="24" cy="14" r="5"/><circle cx="11" cy="20" r="4"/><circle cx="37" cy="20" r="4"/><path d="M15 38c0-6 4-11 9-11s9 5 9 11"/><path d="M4 36c0-5 3-8 7-8M44 36c0-5-3-8-7-8"/></svg></div>
        <div class="value-body"><h2>Teamwork:</h2><p>Collaborating with team members, clients and partners to maintain a high level of communication, accountability and engagement to achieve our common goals</p></div>
      </article>
      <article class="value">
        <div class="value-icon"><svg viewBox="0 0 48 48"><path d="M6 40h36"/><rect x="9" y="28" width="6" height="12"/><rect x="21" y="21" width="6" height="19"/><rect x="33" y="13" width="6" height="27"/><path d="M8 20l10-8 8 5 14-10"/></svg></div>
        <div class="value-body"><h2>Financial Empowerment:</h2><p>We commit ourselves to providing the best retirement solutions to guide our clients toward financial freedom</p></div>
      </article>
      <article class="value">
        <div class="value-icon"><svg viewBox="0 0 48 48"><path d="M24 6a12 12 0 0 0-7 22v6h14v-6A12 12 0 0 0 24 6z"/><path d="M18 39h12M20 43h8"/></svg></div>
        <div class="value-body"><h2>Knowledge:</h2><p>Our team of highly trained and credentialed experts work to educate and lead our clients toward success</p></div>
      </article>
      <article class="value">
        <div class="value-icon"><svg viewBox="0 0 48 48"><path d="M38 18A15 15 0 0 0 10 16"/><path d="M10 8v8h8"/><path d="M10 30a15 15 0 0 0 28 2"/><path d="M38 40v-8h-8"/></svg></div>
        <div class="value-body"><h2>Proactivity:</h2><p>We hold ourselves accountable in anticipating regulatory changes and keeping you and your plan in compliance</p></div>
      </article>
    </div>

    <div class="row row-two">
      <article class="value">
        <div class="value-icon"><svg viewBox="0 0 48 48"><path d="M24 38S8 28 8 18a8 8 0 0 1 16-2 8 8 0 0 1 16 2c0 10-16 20-16 20z"/></svg></div>
        <div class="value-body"><h2>Dedication:</h2><p>We provide exceptional customer service and ensure that we are friendly, timely and responsive whenever corresponding with our clients</p></div>
      </article>
      <article class="value">
        <div class="value-icon"><svg viewBox="0 0 48 48"><path d="M24 5l15 6v11c0 10-7 17-15 21C16 39 9 32 9 22V11z"/><path d="M17 24l5 5 9-10"/></svg></div>
        <div class="value-body"><h2>Security:</h2><p>With an emphasis on high technological standards, we lead you toward peace of mind that your savings and investments are protected</p></div>
      </article>
      <article class="value">
        <div class="value-icon"><svg viewBox="0 0 48 48"><path d="M4 24s8-13 20-13 20 13 20 13-8 13-20 13S4 24 4 24z"/><circle cx="24" cy="24" r="6"/></svg></div>
        <div class="value-body"><h2>Transparency:</h2><p>We take pride in representing the retirement plan industry as an open, honest and socially responsible firm with our clients</p></div>
      </article>
    </div>
  </section>
</div>
</body>
</html>
```